San Francisco Leading Consulting firm - 47Nova Web Design Project

•Create a Web Design
•Uncoded webpage layout design
•2 Pages Design - Homepage + Interior Page

Task Description
Hello, we're looking for a re-design our current website www.47nova-example.com

we have a sample mockup design @

http://47nova.civicpane-example.org/

This shows the layout that we like and also a sample of 6 pictures that would change based on where you mouse over..

6 pictures HOME design needs to be included.

SMART
THOUGHTFUL
FLEXIBLE
CREATIVE SERVICES
TECHNICAL SERVICES
PARTNERS

sites we like:

http://www.brelmoradvisory-example.com/Home.cfm?id=Home
http://www.pixelquarry-example.com/index.html

Our company can be best described as: 100+ employees, cutting-edge, depandable, innovative, strong, smart.

Our Primary focus is: IT Consulting Services and Creative Design services

47Nova LLC is a consulting firm providing creative design, business and technology solutions to both private and public interests.

Established in 1996, 47Nova is a San Francisco based company providing specialists for a range of business needs including:

Creative Design Services
•Print
•Logo Design
•Website Design
•Illustration

and

Business and Technology solutions

•Application Software and Web Development
•Business Process Re-Design (BPR)
•Business/Systems Analysis and Requirement Documentation
•Mentoring and Training
•Network/Hardware Installation Services
•System Design and Architecture
•Vendor Management
•Teamvault Architecture and Implementation

our sample mockup site:

Reason: Due to holiday season, we're not available to work with designers and finilize our design.  

Thank you very much for submitting your design.

We appreciate your time and creativity.   Since, our office is currently closed for holidays, we will be reviewing it in details next week and will make our decision as soon as possible.

It would be great if you could submit any of your changes by Wed next week, so it would be part of our reviews. 

Please see updated wireframe under attachments:  we have some minor updates to our wireframe that we would like you to update your designs, if possible.  

We also encorouge you not to use our standard wireframe and come up with more unique designs.   Everything would be considered when we review your design.

 

Orbita Market(s)

Creative services and professional services clients, including government agencies

Industry/Entity Type

Business

Requirements
Must have
• Clean, professional look, easy navigation

```html
<!DOCTYPE html>
<html lang="en">
<head>
<meta charset="utf-8">
<title>47Nova — We Bridge the Gap</title>
<link href="https://fonts.googleapis.com/css2?family=Arimo:wght@400;700&family=Oswald:wght@400&family=Lobster+Two:ital,wght@1,700&display=swap" rel="stylesheet">
<style>
:root{
  --blue:#1a8cc4;
  --blue-light:#5fbfee;
  --ink:#111;
  --text:#333;
  --grey:#666;
  --rule:#bdbdbd;
  --cream:#efeee4;
  --bg:#fff;
}
*{margin:0;padding:0;box-sizing:border-box}
html,body{width:1200px;height:900px;overflow:hidden;background:var(--bg)}
body{position:relative;font-family:"Arimo",Arial,sans-serif;color:var(--text)}
.abs{position:absolute}

/* header */
.site-header{position:absolute;left:0;top:0;width:1200px;height:90px;border-bottom:3px solid var(--blue);background:var(--bg)}
.brand{position:absolute;left:160px;top:28px;display:flex;align-items:center;gap:10px}
.brand-dot{width:30px;height:30px;border-radius:50%;background:var(--blue-light)}
.brand-name{font-size:30px;color:#555;font-weight:400;letter-spacing:1px}
.main-nav{position:absolute;left:366px;top:36px;display:flex;font-size:13px;color:#333}
.main-nav a{color:inherit;text-decoration:none;padding:0 11px;height:18px;line-height:18px;border-left:1px solid var(--blue)}
.main-nav a:first-child{border-left:none}
.main-nav a.w1{width:79px}.main-nav a.w2{width:133px;text-align:center}.main-nav a.w3{width:145px;text-align:center}.main-nav a.w4{width:86px;text-align:center}.main-nav a.w5{width:90px;text-align:center}
.contact{position:absolute;left:921px;top:10px;font-size:12px;line-height:18px;color:#222;font-style:normal}
.contact .hot{color:var(--blue);font-weight:700}

/* hero */
.hero{position:absolute;left:0;top:90px;width:1200px;height:398px;background:linear-gradient(180deg,#e9e9e9 0%,#d9d9d9 55%,#cfcfcf 100%)}
.hero-title{position:absolute;left:0;width:1200px;top:54px;text-align:center;font-family:"Oswald","Arial Narrow",sans-serif;font-weight:400;font-size:31px;line-height:1;color:var(--ink);letter-spacing:.5px}
.hero-title span{display:inline-block;transform:scaleX(1.12)}
.tag{font-family:"Lobster Two",cursive;font-style:italic;font-weight:700;font-size:22px;line-height:1;color:var(--blue)}
.big{font-family:"Oswald","Arial Narrow",sans-serif;font-weight:400;font-size:43px;line-height:1;color:var(--ink);letter-spacing:1px;transform:scaleX(1.15);transform-origin:left top;white-space:nowrap}
.sub{font-family:"Oswald","Arial Narrow",sans-serif;font-size:30px;line-height:1;color:var(--blue);transform:scaleX(1.08);transform-origin:left top}
.bullets{list-style:none;font-size:14.5px;line-height:24px;color:var(--ink)}
.brain-art{position:absolute;left:465px;top:122px;width:280px;height:195px;border-radius:90px 90px 40px 40px;
  background:radial-gradient(ellipse 60% 55% at 50% 42%,var(--cream) 55%,#7ccaf2 75%,rgba(207,207,207,0) 100%)}

/* clients */
.clients-label{position:absolute;left:130px;top:517px;font-size:19px;font-weight:700;line-height:25px;color:#333}
.client{position:absolute;top:531px;font-size:15px;color:#666;display:flex;align-items:center;gap:5px;white-space:nowrap}
.client i{display:inline-block;width:10px;height:10px;border-radius:50%;background:#777}
.divider{position:absolute;left:124px;width:960px;height:1px;background:var(--rule)}

/* service tiles */
.tile{position:absolute;top:612px;width:280px;height:100px;border:1px solid var(--rule);border-radius:4px;overflow:hidden;background:#fff}
.tile-title{position:absolute;left:6px;top:4px;font-size:15px;color:#555}
.tile-art{position:absolute;bottom:0;height:74px}
.tile-more{position:absolute;right:0;bottom:0}

/* footer */
.copyright{position:absolute;left:126px;top:752px;font-size:12px;color:#333}
.foot-nav{position:absolute;right:119px;top:752px;display:flex;gap:30px;font-size:12px}
.foot-nav a{color:var(--blue);text-decoration:none}
</style>
</head>
<body>

<header class="site-header">
  <div class="brand"><span class="brand-dot"></span><span class="brand-name">47Nova</span></div>
  <nav class="main-nav">
    <a class="w1" href="#">Company</a>
    <a class="w2" href="#">Creative Services</a>
    <a class="w3" href="#">Technical Services</a>
    <a class="w4" href="#">Partners</a>
    <a class="w5" href="#">Contact Us</a>
  </nav>
  <address class="contact">
    2250 Harbor Row, Ste 810<br>
    San Francisco, CA 94107<br>
    <span class="hot">415-555-0147</span><br>
    <span class="hot">info@47nova-example.com</span>
  </address>
</header>

<section class="hero" role="img" aria-label="Faded grey aerial view of the San Francisco skyline">
  <h1 class="hero-title"><span>WE BRIDGE THE GAP</span></h1>

  <div class="abs tag" style="left:152px;top:114px">Left Brain</div>
  <div class="abs big" style="left:153px;top:139px">BUSINESS &amp;</div>
  <div class="abs big" style="left:165px;top:176px">TECHNOLOGY</div>
  <div class="abs sub" style="left:173px;top:217px">Solutions</div>
  <ul class="abs bullets" style="left:152px;top:254px">
    <li>• Application Software and Web Development</li>
    <li>• Business Process Re-Design (BPR)</li>
    <li>• Business/Systems Analysis</li>
    <li>• Mentoring and Training</li>
    <li>... and more</li>
  </ul>

  <div class="brain-art" role="img" aria-label="Two line-drawn brain halves inside glowing blue lightbulb circles"></div>

  <div class="abs tag" style="left:781px;top:114px">Right Brain</div>
  <div class="abs big" style="left:781px;top:139px">CREATIVE</div>
  <div class="abs big" style="left:877px;top:175px">DESIGN</div>
  <div class="abs sub" style="left:873px;top:219px">Services</div>
  <ul class="abs bullets" style="left:781px;top:259px">
    <li>• Print and Package Design</li>
    <li>• Brand and Identity Creation</li>
    <li>• User Experience Design</li>
    <li>• Illustration</li>
    <li>... and more</li>
  </ul>
</section>

<section class="clients">
  <div class="clients-label">Featured<br>Clients</div>
  <svg class="abs" style="left:238px;top:522px" width="22" height="38" viewBox="0 0 22 38"><path d="M2 2 L18 19 L2 36" fill="none" stroke="var(--blue)" stroke-width="6"/></svg>
  <div class="client" style="left:290px"><i></i>Orbita</div>
  <div class="client" style="left:357px">Lumara</div>
  <div class="client" style="left:425px">Vexel</div>
  <div class="client" style="left:490px">Granmotor</div>
  <div class="client" style="left:590px">Arena Nine</div>
  <div class="client" style="left:696px">Telvio</div>
  <div class="client" style="left:782px">Civora</div>
  <div class="client" style="left:882px">Fieldhart</div>
  <div class="client" style="left:995px">Fizzwell</div>
</section>

<div class="divider" style="top:585px"></div>

<section class="tiles">
  <a class="tile" style="left:124px" href="#">
    <span class="tile-title">Creative Services</span>
    <div class="tile-art" role="img" aria-label="Rainbow swirl of translucent coloured ribbons" style="left:80px;width:150px;border-radius:60px 60px 0 0;background:linear-gradient(90deg,#e06ad8,#7b6cf0,#44c7e8,#7be07a,#f0c24a)"></div>
    <svg class="tile-more" width="41" height="41" viewBox="0 0 41 41"><path d="M41 0 V41 H0 Z" fill="var(--blue)"/><path d="M24 31 H34 M29 26 V36" stroke="#fff" stroke-width="2"/></svg>
  </a>
  <a class="tile" style="left:462px" href="#">
    <span class="tile-title">Business &amp; Technical Services</span>
    <div class="tile-art" role="img" aria-label="Cluster of silver metal gears" style="left:45px;width:165px;height:70px;border-radius:50px 50px 0 0;background:radial-gradient(circle at 50% 60%,#c8c8c8,#8a8a8a)"></div>
    <svg class="tile-more" width="41" height="41" viewBox="0 0 41 41"><path d="M41 0 V41 H0 Z" fill="var(--blue)"/><path d="M24 31 H34 M29 26 V36" stroke="#fff" stroke-width="2"/></svg>
  </a>
  <a class="tile" style="left:797px" href="#">
    <span class="tile-title">Partners</span>
    <div class="tile-art" role="img" aria-label="Map of the United States drawn as colourful transit lines" style="left:88px;top:10px;width:140px;height:64px;border-radius:8px;background:linear-gradient(135deg,#f4a3c8,#9fd6f0,#b7e39a,#f7d37a)"></div>
    <svg class="tile-more" width="41" height="41" viewBox="0 0 41 41"><path d="M41 0 V41 H0 Z" fill="var(--blue)"/><path d="M24 31 H34 M29 26 V36" stroke="#fff" stroke-width="2"/></svg>
  </a>
</section>

<div class="divider" style="top:735px"></div>

<footer>
  <p class="copyright">Copyright 2011, 47Nova, LLC All rights reserved.</p>
  <nav class="foot-nav">
    <a href="#">Home</a><a href="#">Company</a><a href="#">Technical Services</a><a href="#">Creative Services</a><a href="#">Partners</a><a href="#">Contact Us</a>
  </nav>
</footer>

</body>
</html>
```